Brusque Premium Men's Shaving Cream Product Label . Cream packaged in a Amber Jar/Black Top Cap.

Please include information ( see Brusque design Template attachment) designed on a Round Top cap. Label Diameter: 3.125" NOTE: Design this First,
Wrap Around Label: 11.3125 x 0.875" (w x h): NOTE: Required latter after selection of Final Design Selection.
Shave Cream packaged in an 8oz Low Profile Amber Jar/Black Top Cap.
Thanks

Target Market(s)

Prime Target-Men Ages 20yrs-65yrs+ and Women 20yrs-65yrs+( they purchase ovr 55% of these Mens care products for partner/spouse/friend.

Industry/Entity Type

Personel Care/Cosmetics/NaturalHealthcare

Other font styles liked:
• At this stage if you would like to submi a desigh that would include both a Top Label and your Wrap-around label on a Amber jar/black top lid. It would be helpful to see how it would look complete. Thanks . Please refer to the updated design Graphic Template for copy and layout . Questions? Let me know. Thanks.Please now use TIMBERHAVEN on label designs. Thanks! Please see image attachment for added Tree Image Vector that can be added to your design instead of the Original Tree Image .

Requirements
Must have
• Look and Feel of a Quality/Premium Mens Skincare Brand with a Masculine feel but attractive to women as well ( not Macho!).Think Unisex with a Male slant.
Nice to have
• Premium/Quality/Natural Skincare & Bodycare Brand
Should not have
• Not Macho. No Cartoony or Barber Tools/Bearded Men Images. Too gimicky and over-hyped!

```html
<!DOCTYPE html>
<html lang="en">
<head>
<meta charset="utf-8">
<title>Brusque Timberhaven Shaving Cream – Top Cap Label</title>
<link href="https://fonts.googleapis.com/css2?family=Cinzel:wght@400;600;700&family=Josefin+Sans:wght@400;600&display=swap" rel="stylesheet">
<style>
  :root {
    --paper: #ffffff;
    --cap-black: #0b0b0b;
    --sand: #bdb39f;
    --sand-soft: #a79e8b;
  }
  * { margin: 0; padding: 0; box-sizing: border-box; }
  html, body {
    width: 1200px;
    height: 1200px;
    overflow: hidden;
    background: var(--paper);
  }
  .canvas {
    position: relative;
    width: 1200px;
    height: 1200px;
  }
  .label-frame {
    position: absolute;
    inset: 0;
  }
  .label-text {
    position: absolute;
    left: 0;
    width: 1200px;
    text-align: center;
    color: var(--sand);
    line-height: 1;
    white-space: nowrap;
  }
  .brand-name {
    top: 326px;
    font-family: "Josefin Sans", sans-serif;
    font-weight: 600;
    font-size: 34px;
    letter-spacing: 7px;
    padding-left: 7px;
  }
  .tree-art {
    position: absolute;
    left: 500px;
    top: 392px;
    width: 200px;
    height: 184px;
    border-radius: 46% 46% 10% 10%;
    background: radial-gradient(ellipse at 50% 38%, #9d9481 0%, #5f5a4f 55%, #1c1b18 100%);
  }
  .product-name {
    top: 610px;
    font-family: "Cinzel", serif;
    font-weight: 700;
    font-size: 66px;
    letter-spacing: 1px;
  }
  .product-type {
    top: 698px;
    font-family: "Cinzel", serif;
    font-weight: 600;
    font-size: 34px;
  }
  .product-type-fr {
    top: 738px;
    font-family: "Cinzel", serif;
    font-weight: 600;
    font-size: 25px;
  }
  .scent-name {
    top: 810px;
    font-family: "Cinzel", serif;
    font-weight: 400;
    font-size: 19px;
  }
  .since-year {
    top: 837px;
    font-family: "Cinzel", serif;
    font-weight: 400;
    font-size: 17px;
    letter-spacing: 1px;
  }
  .net-weight {
    top: 890px;
    font-family: "Cinzel", serif;
    font-weight: 400;
    font-size: 21px;
    letter-spacing: 1px;
  }
</style>
</head>
<body>
<main class="canvas">
  <svg class="label-frame" width="1200" height="1200" viewBox="0 0 1200 1200" aria-hidden="true">
    <circle class="cap-disc" cx="600" cy="600" r="384" fill="var(--cap-black)"/>
    <circle class="ring-outer" cx="600" cy="600" r="375" fill="none" stroke="var(--sand)" stroke-width="2.5"/>
    <circle class="ring-dots" cx="600" cy="600" r="364" fill="none" stroke="var(--sand)" stroke-width="4.5" stroke-linecap="round" stroke-dasharray="0 7.6"/>
    <circle class="ring-inner" cx="600" cy="600" r="353" fill="none" stroke="var(--sand)" stroke-width="2.5"/>
    <path class="ring-thin" d="M725 336 A292 292 0 0 1 683 880" fill="none" stroke="var(--sand)" stroke-width="1.5"/>
    <path class="ring-thin" d="M517 880 A292 292 0 0 1 475 336" fill="none" stroke="var(--sand)" stroke-width="1.5"/>
    <line class="divider" x1="512" y1="788" x2="688" y2="788" stroke="var(--sand-soft)" stroke-width="1.5"/>
    <line class="year-dash" x1="522" y1="846" x2="548" y2="846" stroke="var(--sand)" stroke-width="1.5"/>
    <line class="year-dash" x1="652" y1="846" x2="678" y2="846" stroke="var(--sand)" stroke-width="1.5"/>
  </svg>

  <div class="label-text brand-name">BRUSQUE</div>
  <div class="tree-art" role="img" aria-label="Illustration of a leafy tree with spreading roots"></div>
  <div class="label-text product-name">Timberhaven</div>
  <div class="label-text product-type">Shaving Cream</div>
  <div class="label-text product-type-fr">Crème De Rasage</div>
  <div class="label-text scent-name">Cedarmoss Reserve</div>
  <div class="label-text since-year">1935</div>
  <div class="label-text net-weight">150g (5.3 oz)</div>
</main>
</body>
</html>
```